We need a striking new book cover for a new book.

This book presents a modern concept based on the latest discoveries in the field of molecular genetics and nuclear physics. It helps us to understand the direction in which the universe, the world and each of us as individuals could be heading given the impact of laws of physics and evolution.

Book Title: The Quiet Lantern Doctrine
Author: Radosław Wenta

The text to go on the front cover is as follows :

The Quiet Lantern Doctrine
Radosław Wenta
is a scientist, author, publisher and a member of ORVIK

The photograph of the author uploaded should go on the back cover.
The text to go on the back cover is as follows:

This book presents a modern concept based on the latest discoveries in the field of molecular genetics and nuclear physics. It helps us to understand the direction in which the universe, the world, and each of us as individuals could be heading, given the impact of the laws of physics, and evolution. Entropy (law of physics) implies increasing chaos and that our universe inclines towards ever greater disorder.
Evolution means that everything evolves into more and more complex structures.

When entropy and evolution work together they create further sophistication in life on Earth. Chaos-driven evolution has not only created gravity, i.e. cosmic objects such as stars and planets, but it is also the driving force behind the changes on Earth now, and governs not just the universe and our planet, but also our lives and even our bodies.

Evolution sets goals while entropy is the driving force. Societies are becoming more open and progressive. Our freedom is increasing. Evolution keeps bringing more diversification. Scientific progress is accelerating and reducing the need for religions. We are seeing progress in social awareness and morality.
There are constant transfers of energy powering all changes in the micro- and macro- scale, as well as the everyday life of each of us.
Our world is at a major junction and our choices will benefit or taint future generations.

Radosław Wenta, is a scientist, author, publisher and a member of ORVIK.
He studied at both Brenmoor University and Tallowfield University. Having completed his studies in Biological Chemistry, he then further broadened his scientific experience whilst working in digital molecular genetics in the UK. In Poland he has conducted extensive research in the field of auto-immune diseases. He also holds an MBA. He is the author of a number of scientific works and guide books.

```html
<!DOCTYPE html>
<html lang="en">
<head>
<meta charset="utf-8">
<title>The Quiet Lantern Doctrine — Front Cover</title>
<link rel="stylesheet" href="https://fonts.googleapis.com/css2?family=Josefin+Sans:wght@300;400&display=swap">
<style>
  :root {
    --page-bg: #e9e6e1;
    --cover-black: #03070d;
    --cover-navy: #0a1430;
    --cover-blue: #1b2f8c;
    --cover-teal: #0f4a46;
    --cover-green: #1f6b4e;
    --cover-mist: #2f7a6a;
    --type-light: #f1f1ec;
    --type-soft: #dcdcd5;
  }
  * { margin: 0; padding: 0; box-sizing: border-box; }
  html, body {
    width: 1200px;
    height: 1200px;
    overflow: hidden;
    background: var(--page-bg);
  }
  .canvas {
    position: relative;
    width: 1200px;
    height: 1200px;
  }
  .book-cover {
    position: absolute;
    left: 285px;
    top: 95px;
    width: 630px;
    height: 1010px;
    overflow: hidden;
    background: var(--cover-black);
    color: var(--type-light);
    font-family: "Josefin Sans", sans-serif;
    text-align: center;
  }
  .cover-art {
    position: absolute;
    inset: 0;
    background:
      radial-gradient(ellipse 45% 30% at 80% 50%, rgba(27,47,140,0.85), transparent 70%),
      radial-gradient(ellipse 40% 25% at 35% 55%, rgba(47,122,106,0.55), transparent 70%),
      radial-gradient(ellipse 55% 25% at 25% 75%, rgba(31,107,78,0.75), transparent 70%),
      radial-gradient(ellipse 50% 20% at 75% 88%, rgba(15,74,70,0.8), transparent 70%),
      radial-gradient(ellipse 60% 18% at 60% 20%, rgba(15,74,70,0.45), transparent 70%),
      linear-gradient(180deg, var(--cover-black) 0%, var(--cover-navy) 40%, #061a1e 75%, var(--cover-black) 100%);
  }
  .cover-title {
    position: absolute;
    left: 0;
    right: 0;
    top: 322px;
    font-weight: 300;
    font-size: 38px;
    line-height: 54px;
    letter-spacing: 0.12em;
    text-transform: uppercase;
    padding-left: 0.12em;
  }
  .cover-author {
    position: absolute;
    left: 0;
    right: 0;
    top: 838px;
    font-weight: 300;
    font-size: 33px;
    letter-spacing: 0.1em;
    text-transform: uppercase;
  }
  .cover-author-credit {
    position: absolute;
    left: 0;
    right: 0;
    top: 886px;
    font-weight: 400;
    font-size: 12px;
    line-height: 17px;
    letter-spacing: 0.04em;
    text-transform: uppercase;
    color: var(--type-soft);
  }
</style>
</head>
<body>
  <main class="canvas">
    <section class="book-cover">
      <div class="cover-art" role="img" aria-label="Abstract cosmic marbled texture in deep navy, blue and green with scattered star-like specks"></div>
      <h1 class="cover-title">The Quiet Lantern<br>Doctrine</h1>
      <p class="cover-author">Radosław Wenta</p>
      <p class="cover-author-credit">Scientist, author, publisher and<br>a member of ORVIK</p>
    </section>
  </main>
</body>
</html>
```